Product Photographer in Jacksonville Florida need marketing post card

need postcard to mail and hand deliver to prospects. Goal is to get more product photography jobs into studio. I shoot jewelry, food, wine, art, products, clothes, etc. Include my logo, phone, email, Black font, white background, clean, cool, modern,...i like the fint that Tallowmere Quill mag uses on cover

Target Market(s)

artist that design & create jewlery, painting, pottery, Restaurants food photos,

Industry/Entity Type

Jewelry

Font styles to use
Serif

Colors
ffffff

Requirements
Must have
• I like font like Lumen Magazine title, Tallowmere Quill mag title
• 1-3 cool product images. maybe jewlery, food, clothes
• cool, clean, modern, edgy ...not corporate feel.
• white back ground, black text
• image is everything
Nice to have
• clean lots of white space ok.
Should not have
• no bright colors,

```html
<!DOCTYPE html>
<html lang="en">
<head>
<meta charset="utf-8">
<title>Corin Vale Photography – Postcard</title>
<link rel="stylesheet" href="https://fonts.googleapis.com/css2?family=Cinzel:wght@400;600&family=Cormorant+Garamond:wght@500;600&display=swap">
<style>
  :root {
    --page-bg: #e9e9e9;
    --card-bg: #ffffff;
    --ink: #1a1a1a;
    --ink-soft: #4a4a4a;
    --rule: #2b2b2b;
    --tone-white: #fbfbfb;
    --tone-pale: #ececec;
    --tone-light: #d2d2d2;
    --tone-mid: #9a9a9a;
    --tone-deep: #4a4a4a;
    --tone-black: #262626;
    --shadow: rgba(0,0,0,0.18);
  }
  * { box-sizing: border-box; margin: 0; padding: 0; }
  html, body { width: 900px; height: 1200px; overflow: hidden; }
  body {
    background: var(--page-bg);
    font-family: "Cormorant Garamond", "Times New Roman", serif;
    color: var(--ink);
    position: relative;
  }
  .postcard {
    position: absolute;
    left: 60px;
    width: 780px;
    height: 525px;
    background: var(--card-bg);
    box-shadow: 0 6px 18px var(--shadow);
    overflow: hidden;
  }
  .postcard--front { top: 45px; }
  .postcard--back { top: 615px; }

  /* Brand name (logo stand-in) */
  .brand {
    display: flex;
    align-items: center;
    gap: 12px;
    font-family: "Cinzel", "Times New Roman", serif;
    font-weight: 400;
    color: var(--ink);
    text-transform: uppercase;
  }
  .brand__square { width: 38px; height: 38px; background: var(--ink); flex: none; }
  .brand__name { line-height: 1.15; letter-spacing: 2px; }

  /* Front */
  .front__brand { position: absolute; left: 45px; top: 40px; z-index: 2; }
  .front__brand .brand__square { width: 46px; height: 46px; }
  .front__brand .brand__name { font-size: 24px; }
  .front__photo {
    position: absolute;
    right: 0; top: 0;
    width: 66%;
    height: 100%;
    background: radial-gradient(ellipse 95% 110% at 100% 0%,
      var(--tone-black) 0%,
      var(--tone-deep) 18%,
      var(--tone-mid) 34%,
      var(--tone-light) 52%,
      var(--tone-pale) 72%,
      var(--tone-white) 100%);
    -webkit-mask-image: linear-gradient(90deg, transparent 0%, #000 30%);
    mask-image: linear-gradient(90deg, transparent 0%, #000 30%);
  }
  .front__contact {
    position: absolute;
    left: 45px; bottom: 60px;
    z-index: 2;
    font-size: 22px;
    font-weight: 500;
    letter-spacing: 0.5px;
    line-height: 1.3;
    text-transform: uppercase;
  }

  /* Back */
  .back__heading {
    position: absolute;
    left: 45px; top: 42px;
    width: 380px;
    text-align: center;
    font-family: "Cinzel", "Times New Roman", serif;
  }
  .back__title { font-size: 23px; letter-spacing: 1.5px; }
  .back__subtitle {
    display: flex; align-items: center; gap: 14px;
    justify-content: center;
    margin-top: 6px;
    font-size: 20px; letter-spacing: 2px;
  }
  .back__subtitle::before, .back__subtitle::after {
    content: ""; width: 90px; height: 1.5px; background: var(--rule);
  }
  .services {
    position: absolute;
    left: 75px; top: 150px;
    display: flex; gap: 30px;
  }
  .service-image { width: 96px; height: 96px; border-radius: 50%; border: 2px solid var(--ink-soft); }
  .service-image--jewelry { background: radial-gradient(circle, #ffffff 0%, #d8d8d8 70%, #a8a8a8 100%); }
  .service-image--apparel { background: radial-gradient(circle, #f6f6f6 0%, #bdbdbd 70%, #8a8a8a 100%); }
  .service-image--wine { background: linear-gradient(180deg, #dfe7ee 0%, #9fb4c6 100%); }
  .back__services-text {
    position: absolute;
    left: 45px; top: 275px;
    width: 400px;
    text-align: center;
    font-size: 21px; font-weight: 600;
    letter-spacing: 0.5px;
    text-transform: uppercase;
  }
  .back__contact {
    position: absolute;
    left: 45px; bottom: 40px;
    list-style: none;
    font-size: 19px; font-weight: 500;
    line-height: 1.35;
    text-transform: uppercase;
  }
  .back__contact li { display: flex; align-items: center; gap: 8px; }
  .back__contact svg { width: 16px; height: 16px; flex: none; }

  .stamp-box {
    position: absolute;
    right: 50px; top: 45px;
    width: 110px; height: 120px;
    border: 2px solid var(--rule);
  }
  .address-lines { position: absolute; right: 50px; top: 215px; width: 270px; }
  .address-lines span { display: block; height: 1.5px; background: var(--rule); margin-bottom: 42px; }
  .back__brand { position: absolute; right: 50px; bottom: 38px; }
  .back__brand .brand__square { width: 26px; height: 26px; }
  .back__brand .brand__name { font-size: 13px; }
</style>
</head>
<body>

<section class="postcard postcard--front">
  <div class="front__photo" role="img" aria-label="Black and white beauty portrait photograph of a model with dark hair, filling the right side of the card"></div>
  <div class="brand front__brand">
    <span class="brand__square"></span>
    <span class="brand__name">Corin Vale<br>Photography</span>
  </div>
  <div class="front__contact">
    <p>studio@corinvale-photo.com</p>
    <p>corinvale-photo.com</p>
  </div>
</section>

<section class="postcard postcard--back">
  <div class="back__heading">
    <p class="back__title">Corin Vale Photography</p>
    <p class="back__subtitle">Product</p>
  </div>

  <div class="services">
    <div class="service-image service-image--jewelry" role="img" aria-label="Product photo of a diamond ring"></div>
    <div class="service-image service-image--apparel" role="img" aria-label="Product photo of a bow tie"></div>
    <div class="service-image service-image--wine" role="img" aria-label="Product photo of wine glasses"></div>
  </div>

  <p class="back__services-text">I shoot jewelry, food, wine, art, products, clothes</p>

  <ul class="back__contact">
    <li>
      <svg viewBox="0 0 16 16" aria-hidden="true"><circle cx="8" cy="8" r="7" fill="none" stroke="#1a1a1a" stroke-width="1.3"/><path d="M5.3 4.5l1.4 1.6-.8 1c.5 1 1.2 1.7 2.1 2.2l1-.8 1.6 1.4-.9 1.2c-2.6-.4-4.9-2.7-5.3-5.4z" fill="#1a1a1a"/></svg>
      (555) 014-2876
    </li>
    <li>
      <svg viewBox="0 0 16 16" aria-hidden="true"><rect x="1.5" y="3.5" width="13" height="9" fill="none" stroke="#1a1a1a" stroke-width="1.3"/><path d="M1.5 3.5L8 9l6.5-5.5" fill="none" stroke="#1a1a1a" stroke-width="1.3"/></svg>
      studio@corinvale-photo.com
    </li>
    <li>
      <svg viewBox="0 0 16 16" aria-hidden="true"><circle cx="8" cy="8" r="6.5" fill="none" stroke="#1a1a1a" stroke-width="1.3"/><ellipse cx="8" cy="8" rx="2.8" ry="6.5" fill="none" stroke="#1a1a1a" stroke-width="1.1"/><path d="M1.5 8h13" stroke="#1a1a1a" stroke-width="1.1"/></svg>
      corinvale-photo.com
    </li>
  </ul>

  <div class="stamp-box"></div>
  <div class="address-lines"><span></span><span></span><span></span></div>

  <div class="brand back__brand">
    <span class="brand__square"></span>
    <span class="brand__name">Corin Vale<br>Photography</span>
  </div>
</section>

</body>
</html>
```